Etiketten für Weinflasche
Zielgruppe
HANDARBEIT
HAT SEELE.
»80 % gibt uns die Natur vor,
für die restlichen 20 % geben wir alles!«
Volker Brandhuber
Seit über 125 Jahren ist die Rotweinstadt Ingelheim Sitz unseres Familienbetriebes. Im alten Ober-Ingelheimer Schulhaus gelegen, betreiben wir das Weingut in der nunmehr 5. Generation. Unser hoher Qualitätsanspruch und Traditionsbewusstsein wird von Kennern eines guten Weines geschätzt. Zusammen mit der Natur und so schonend wie möglich bewirtschaften wir die rund 15 ha Weinberge in den besten Lagen Ingelheims.
Ganz in der Tradition Karls des Großen, der die Rotweinreben um 800 n. Chr. nach Ingelheim brachte, sind die Spät- und Frühburgunder die Spezialitäten unseres Hauses. Seit 2015 sind wir Träger des „Goldenen Traubenpokals' des Weinkulturmagazins Korkla. Das macht uns stolz und gibt uns Energie. Auch die Rieslinge und die weißen Burgundersorten stehen im Fokus und werden mit viel Gefühl zum Detail gekeltert. Den geselligen Mittelpunkt des Weinguts bildet unser über hundert Jahre alter Pavillon. Er steht symbolisch für uns als gastliche Weinfamilie und vertritt unser Weingut auch nach außen auf unseren Etiketten.
Aufgabenstellung
Ein Wein für FRANKFURTER
Wir möchten für einen führende Marktis-Gruppe in Frankfurt eine Weißwein-Sonderedition entwickeln.
Es soll ein Label sein, womit sich jeder Frankfurter identifizieren kann (Skyline gab es schon mal ist aber nicht ausgeschlossen) und dazu animiert wird die Weinflasche blind zu kaufen.
Die Rebsorte soll auf dem Vorderetikett genannt werden. Es ist ein Grauburgunder oder Grauer Burgunder. Der Wein soll ein schönes Mitbringsel oder auch für den eigenen Genuss sein. Die Flasche wird sich im mittleren Preissegment bewegen +/- 10€ im Verkauf. Zielgruppe 40-65 Jahre alt.
Es gibt drei mögliche Etikettengrößen.
Variante 1: Bestehendes Brandhuber-Etikett mit Streifen (wie in der Anlage)
Variante 2: Vorder- und Rückenetikett mit je 7cm x 7cm oder
Variante 3: Vorderetikett (9cm Breit x 6cm hoch) und Rückenetikett (7cm Breit x 6cm hoch)
Die Rückseite kann ein : gestalterisches Element vom Vorderetikett beinhalten, ist aber durch die gesetzlichen Angaben und den EAN-Code schon ziemlich ausgelastet. Es zum größten Teil um das Vorderetikett.
Die Kapsel am Flaschenhals ist weiß mit gelber Markierung und es gibt eine gelbe Kapsel mit weißer Markierung. Diese ist beiden sind fix, da der Wein schon abgefüllt ist. Es ist eine Burgunderflasche.
Ein Flaschenbild stelle ich zur Verfügung.

```html
<!DOCTYPE html>
<html lang="de">
<head>
<meta charset="utf-8">
<title>Grauburgunder – Vorderetikett</title>
<link href="https://fonts.googleapis.com/css2?family=Montserrat:wght@800&family=EB+Garamond&display=swap" rel="stylesheet">
<style>
  :root {
    --backdrop: #eaeaea;
    --ochre: #dc9c0a;
    --ochre-deep: #c98a06;
    --ochre-light: #e9b547;
    --ink: #1d1d1b;
    --paper: #ffffff;
    --water: #dcdcdc;
  }
  html, body {
    margin: 0;
    padding: 0;
    width: 1061px;
    height: 1200px;
    overflow: hidden;
    background: var(--backdrop);
  }
  .canvas {
    position: relative;
    width: 1061px;
    height: 1200px;
  }
  .label {
    position: absolute;
    left: 100px;
    top: 169px;
    width: 860px;
    height: 862px;
    background: var(--paper);
    box-shadow: 2px 3px 4px rgba(0,0,0,0.25);
    overflow: hidden;
  }
  .label__band {
    position: absolute;
    left: 0;
    top: 0;
    width: 860px;
    height: 326px;
    background: var(--ochre);
  }
  .label__brand {
    position: absolute;
    left: 92px;
    top: 158px;
    margin: 0;
    font-family: "EB Garamond", serif;
    font-weight: 400;
    font-size: 30px;
    letter-spacing: 0.5px;
    color: var(--ink);
    line-height: 1;
  }
  .label__skyline {
    position: absolute;
    left: 57px;
    top: 103px;
    width: 803px;
    height: 226px;
  }
  .label__river {
    position: absolute;
    left: 0;
    top: 326px;
    width: 860px;
    height: 536px;
  }
  .label__variety {
    position: absolute;
    left: 80px;
    top: 432px;
    margin: 0;
    font-family: "Montserrat", sans-serif;
    font-weight: 800;
    font-size: 139px;
    line-height: 123px;
    letter-spacing: -1px;
    color: var(--ink);
  }
</style>
</head>
<body>
<main class="canvas">
  <section class="label">
    <div class="label__band"></div>
    <p class="label__brand">BRANDHUBER</p>
    <svg class="label__skyline" viewBox="0 0 803 226" role="img" aria-label="Gezeichnete Frankfurter Skyline mit Hochhäusern, Eisernem Steg und Altstadt am Mainufer">
      <defs>
        <linearGradient id="skylineTone" x1="0" y1="0" x2="0" y2="1">
          <stop offset="0" stop-color="var(--ochre)"/>
          <stop offset="0.45" stop-color="var(--ochre-light)"/>
          <stop offset="1" stop-color="var(--ochre-deep)"/>
        </linearGradient>
      </defs>
      <path d="M0 200 L120 160 L270 120 L410 20 L450 0 L480 60 L560 150 L700 130 L803 100 L803 226 L0 226 Z" fill="url(#skylineTone)"/>
    </svg>
    <svg class="label__river" viewBox="0 0 860 536" role="img" aria-label="Stilisierte Wasserfläche des Mains mit hellgrauen Wellenstreifen">
      <defs>
        <linearGradient id="riverTone" x1="1" y1="0" x2="0" y2="1">
          <stop offset="0" stop-color="var(--water)"/>
          <stop offset="0.7" stop-color="#ececec"/>
          <stop offset="1" stop-color="var(--paper)"/>
        </linearGradient>
      </defs>
      <path d="M132 0 L860 0 L860 500 L780 510 L620 500 L560 420 L470 300 L310 200 L220 80 Z" fill="url(#riverTone)"/>
    </svg>
    <h1 class="label__variety">GRAU<br>BURG<br>UNDER</h1>
  </section>
</main>
</body>
</html>
```